Brookvine Estates Business Card

Business Card:

Somewhere on front of card, please include Broker License Number: 5839261

Website is BrookvineEstates.com

Address is:
7216 Orchardpine Ave E
Saginaw, MI 48517

I'll let you use creative freedom on the rest; we obviously need Name, Title, Email (@BrookvineEstates.com), Office Phone, Cell Phone.

Don't want any special die-cutting, just a standard size business card.

On the back, include a place for the date and time of an appointment to be written in pen.

Industry/Entity Type

Business

Requirements
Must have
• Our logo, attached to email.

```html
<!DOCTYPE html>
<html lang="en">
<head>
<meta charset="utf-8">
<title>Brookvine Estates Business Card</title>
<link rel="stylesheet" href="https://fonts.googleapis.com/css2?family=Ubuntu:wght@400;500;700&display=swap">
<style>
  :root {
    --navy: #2f1f6f;
    --band-grey: #b9b9bb;
    --paper: #ffffff;
    --backdrop: #b0aeaf;
    --name-grey: #b8b6c4;
    --white: #ffffff;
  }
  html, body {
    margin: 0;
    padding: 0;
    width: 1200px;
    height: 1200px;
    overflow: hidden;
    background: var(--backdrop);
    font-family: "Ubuntu", sans-serif;
  }
  .canvas { position: relative; width: 1200px; height: 1200px; }
  .card { position: absolute; overflow: hidden; }

  /* Appointment side */
  .card-appointment {
    left: 238px; top: 119px; width: 713px; height: 418px;
    background: var(--paper);
  }
  .appointment-tab {
    position: absolute; left: 0; top: 101px; width: 362px; height: 47px;
  }
  .appointment-title {
    position: absolute; left: 48px; top: 111px; margin: 0;
    font-size: 23px; font-weight: 700; letter-spacing: 1px; color: var(--navy);
  }
  .brand-name {
    position: absolute; margin: 0; font-weight: 500; white-space: nowrap;
  }
  .card-appointment .brand-name {
    right: 54px; top: 76px; font-size: 38px; color: var(--navy);
  }
  .write-row {
    position: absolute; left: 48px; right: 48px; display: flex; align-items: flex-end;
    font-size: 19px; color: var(--navy);
  }
  .write-row .label { padding-right: 4px; }
  .write-row .line { flex: 1; border-bottom: 2px solid var(--navy); height: 18px; }
  .write-row .label + .line + .label { padding-left: 6px; }
  .row-for { top: 211px; }
  .row-when { top: 281px; }
  .row-when .line-date { flex: 1.42; }
  .license-band {
    position: absolute; left: 0; bottom: 0; width: 100%; height: 56px;
    background: var(--navy); color: var(--white);
    display: flex; align-items: center; justify-content: center;
    font-size: 18px;
  }

  /* Contact side */
  .card-contact {
    left: 230px; top: 643px; width: 714px; height: 418px;
    background: var(--navy);
  }
  .card-contact .brand-name {
    left: 34px; top: 166px; font-size: 38px; color: var(--white);
  }
  .person-name {
    position: absolute; left: 365px; top: 89px; margin: 0;
    font-size: 24px; font-weight: 700; color: var(--name-grey);
  }
  .person-title {
    position: absolute; left: 365px; top: 125px; margin: 0;
    font-size: 16px; color: var(--name-grey);
  }
  .contact-list {
    position: absolute; left: 366px; top: 190px; margin: 0; padding: 0; list-style: none;
    color: var(--white); font-size: 18.5px; line-height: 23px;
  }
  .contact-list li { display: flex; align-items: center; gap: 12px; }
  .contact-list svg { width: 16px; height: 16px; flex: none; }
  .address-band {
    position: absolute; left: 0; bottom: 0; width: 100%; height: 54px;
    background: var(--band-grey); color: var(--navy);
    display: flex; align-items: center; justify-content: center;
    font-size: 19px;
  }
</style>
</head>
<body>
<main class="canvas">

  <section class="card card-appointment">
    <svg class="appointment-tab" viewBox="0 0 362 47" aria-hidden="true">
      <polygon points="0,0 348,0 362,47 0,47" fill="var(--band-grey)"/>
    </svg>
    <h2 class="appointment-title">YOUR&nbsp; APPOINTMENT</h2>
    <p class="brand-name">Brookvine Estates</p>
    <div class="write-row row-for"><span class="label">For</span><span class="line"></span></div>
    <div class="write-row row-when">
      <span class="label">Date:</span><span class="line line-date"></span>
      <span class="label">Time:</span><span class="line"></span>
    </div>
    <div class="license-band">Broker License Number: 5839261</div>
  </section>

  <section class="card card-contact">
    <p class="brand-name">Brookvine Estates</p>
    <h1 class="person-name">Your XYZ Name</h1>
    <p class="person-title">Your Title</p>
    <ul class="contact-list">
      <li>
        <svg viewBox="0 0 16 16" aria-hidden="true"><rect x="4" y="1" width="8" height="14" rx="1.5" fill="none" stroke="#c9c7d6" stroke-width="1.6"/><circle cx="8" cy="12.3" r="0.9" fill="#c9c7d6"/></svg>
        +00 555 201 7788
      </li>
      <li>
        <svg viewBox="0 0 16 16" aria-hidden="true"><path d="M1 6 Q8 1 15 6 L13 7.5 L11 6 L5 6 L3 7.5 Z" fill="#c9c7d6"/><rect x="3" y="8" width="10" height="6" rx="1" fill="#c9c7d6"/></svg>
        +00 555 309 4422
      </li>
      <li>
        <svg viewBox="0 0 16 16" aria-hidden="true"><circle cx="8" cy="8" r="6.5" fill="none" stroke="#c9c7d6" stroke-width="1.4"/><ellipse cx="8" cy="8" rx="2.8" ry="6.5" fill="none" stroke="#c9c7d6" stroke-width="1.2"/><line x1="1.5" y1="8" x2="14.5" y2="8" stroke="#c9c7d6" stroke-width="1.2"/></svg>
        www.brookvineEstates.com
      </li>
      <li>
        <svg viewBox="0 0 16 16" aria-hidden="true"><rect x="1" y="3.5" width="14" height="9" fill="#c9c7d6"/><polyline points="1,3.5 8,9 15,3.5" fill="none" stroke="var(--navy)" stroke-width="1.2"/></svg>
        yourname@brookvineEstates.com
      </li>
    </ul>
    <div class="address-band">7216 Orchardpine Ave E Saginaw, MI 48517</div>
  </section>

</main>
</body>
</html>
```